Real Estate Investor needs awesome business card design

I invest in real estate, focused on multi-family properties, and I need a business card to hand out to potential partners. I prefer simple, clean designs, but it needs to stand out, so I'd like there to be a bit of red in the design as well.

It should include this information:

Front
Calder Whitby
Real Estate Investor
Direct phone: 501-555-0187
Email: calderjwhitby@mailbox-example.net
Headshot (Picture), I've uploaded a few, just pick the one you think looks best with your design. You can remove the background from the headshot image if it looks better.

Back
The back of the card's design should flow and be congruent with the front. On the back I want to put an inspirational quote or question. There will be different ones depending on the card, so I'll need the original file so I can edit it in the end.

For now, use “The Pessimist Sees Difficulty In Every Opportunity. The Optimist Sees The Opportunity In Every Difficulty.” -Edmund Halvorsen

Target Market(s)

Investors

Industry/Entity Type

Real Estate

Contact Information for Business Card

Front
Calder Whitby
Real Estate Investor

Back
The back of the card's design should flow and be congruent with the front. On the back I want to put an inspirational quote or question. There will be different ones depending on the card, so I'll need the original file so I can edit it in the end. I've uploaded some EXAMPLES of business cards with quotes on them. Don't copy but feel free to use them as inspiration.

The design will be printed on "ZAP sized" business cards
1039 x 697 pixels
with rounded corners

Font styles to use
Serif
Decorative
Script

Colors
ec1f27

Requirements
Must have
• Headshot, name, and other information in it.
• 1039 x 697 pixels
• Rounded corners
• Clean design that pops. I'm open to see any color background, including black.
• Headshots can be located here: https://www.filecrate-example.com/sh/8kx2vq71ld0pa3z/BQQTXL7mrrf9eT3Kq0HhgkLm2b?dl=0
Nice to have
• It would be awesome if the design included a personal signature or monogram, but if not I'll get a personal logo developed later and the card redesigned if I think it needs it.
Should not have
• Cluttered design

```html
<!DOCTYPE html>
<html lang="en">
<head>
<meta charset="utf-8">
<title>Calder Whitby – Business Card</title>
<link rel="stylesheet" href="https://fonts.googleapis.com/css2?family=Roboto+Condensed:wght@400;700&family=Roboto:wght@300;400&display=swap">
<style>
  :root {
    --stage-light: #ffffff;
    --stage-dark: #e4e5e6;
    --card-white: #ffffff;
    --stripe: #e9e9ea;
    --card-black: #1e1f1f;
    --ink: #1b1b1b;
    --ink-soft: #333333;
    --accent-red: #ec1f27;
    --white: #ffffff;
    --watermark: #2b2c2c;
    --photo-tone-a: #c9a48f;
    --photo-tone-b: #2a3040;
  }
  * { margin: 0; padding: 0; box-sizing: border-box; }
  html, body { width: 1200px; height: 1000px; overflow: hidden; }
  body {
    position: relative;
    background: radial-gradient(ellipse at 50% 45%, var(--stage-light) 0%, var(--stage-dark) 100%);
    font-family: "Roboto", sans-serif;
  }
  .card {
    position: absolute;
    top: 337px;
    width: 513px;
    height: 331px;
    border-radius: 30px;
    overflow: hidden;
    box-shadow: 0 4px 16px rgba(0,0,0,0.28);
  }
  .card-front {
    left: 70px;
    background-color: var(--card-white);
    background-image: repeating-linear-gradient(90deg, transparent 0 10px, var(--stripe) 10px 11px);
  }
  .card-back { left: 614px; background: var(--card-black); }

  .headshot-frame {
    position: absolute;
    left: 39px; top: 48px;
    width: 234px; height: 234px;
    border-radius: 50%;
    border: 6px solid var(--ink);
    background: var(--card-white);
    padding: 4px;
  }
  .headshot {
    width: 100%; height: 100%;
    border-radius: 50%;
    background: linear-gradient(180deg, #f4f1ef 0%, var(--photo-tone-a) 45%, var(--photo-tone-b) 100%);
  }

  .identity {
    position: absolute;
    left: 275px; top: 62px;
    width: 238px;
    text-align: center;
    color: var(--ink);
  }
  .monogram {
    font-family: "Roboto Condensed", sans-serif;
    font-weight: 700;
    font-size: 60px;
    line-height: 96px;
    height: 96px;
    letter-spacing: -2px;
    color: var(--ink);
  }
  .name {
    margin-top: 14px;
    font-family: "Roboto Condensed", sans-serif;
    font-weight: 700;
    font-size: 20px;
    line-height: 22px;
    letter-spacing: 0.3px;
  }
  .name-last { color: var(--accent-red); }
  .role {
    font-weight: 300;
    font-size: 16px;
    line-height: 20px;
    color: var(--ink-soft);
  }
  .contact {
    margin-top: 12px;
    font-weight: 300;
    font-size: 15px;
    line-height: 18px;
    color: var(--ink-soft);
  }
  .contact .email { font-size: 13px; }

  .watermark {
    position: absolute;
    left: 170px; top: 30px;
    font-family: "Roboto Condensed", sans-serif;
    font-weight: 700;
    font-size: 190px;
    line-height: 240px;
    color: var(--watermark);
    letter-spacing: -8px;
  }
  .quote {
    position: absolute;
    left: 0; top: 100px;
    width: 100%;
    text-align: center;
    font-family: "Roboto Condensed", sans-serif;
    font-weight: 700;
    font-size: 22px;
    line-height: 27.5px;
    color: var(--white);
    text-transform: uppercase;
  }
  .quote-author {
    position: absolute;
    left: 0; top: 236px;
    width: 100%;
    text-align: center;
    font-family: "Roboto Condensed", sans-serif;
    font-weight: 700;
    font-size: 22px;
    color: var(--accent-red);
    text-transform: uppercase;
  }
</style>
</head>
<body>
  <section class="card card-front">
    <div class="headshot-frame">
      <div class="headshot" role="img" aria-label="Headshot of Calder Whitby"></div>
    </div>
    <div class="identity">
      <div class="monogram">CW</div>
      <div class="name">CALDER <span class="name-last">WHITBY</span></div>
      <div class="role">Real Estate Investor</div>
      <div class="contact">
        <div class="phone">501-555-0187</div>
        <div class="email">calderjwhitby@mailbox-example.net</div>
      </div>
    </div>
  </section>

  <section class="card card-back">
    <div class="watermark" aria-hidden="true">CW</div>
    <blockquote class="quote">
      “The pessimist sees difficulty<br>
      in every opportunity.<br>
      The optimist sees the opportunity<br>
      in every difficulty.”
    </blockquote>
    <div class="quote-author">-Edmund Halvorsen</div>
  </section>
</body>
</html>
```